Business Card for Managing Partner Investment Fund

To create a business card template for an investment fund manager. Business card should be more professional in nature, not too colorful, more upscale, and created using the attached logos and fund name files. I would prefer a black or gray color scheme, but am open to the use of color as well. I would prefer a double sided business card, but open to single sided business card designs as well. The business card should include: name, title, and contact information, as well as logo and company name. I would prefer a more stream-lined, simple business card design.
Updates
Address: 4136 NE 19th Ter. Ocala, FL 34470
Email: travis48@quillnet-mail.com
Phone: 561-374-9186
Title: managing partner
Name: Travis Whitlow
Fund Name: Emberfall Capital
Logos can be found in files attached to the brief
Target Market(s)
potential investors, other fund managers
Industry/Entity Type
Finance
Contact Information for Business Card
Name on card: Travis Whitlow
Title: Managing Partner
Font styles to use
Colors
Designer to choose colors to be used in the design.
Requirements
Must have
- Phone number
- email address
- physical address
- title
- name
- logo
- Fund name
Nice to have
- simple layout
Should not have
- too many colors, busy fonts,

```html
<!DOCTYPE html>
<html lang="en">
<head>
<meta charset="utf-8">
<title>Emberfall Capital – Business Card</title>
<link href="https://fonts.googleapis.com/css2?family=Poppins:wght@400;500;600&display=swap" rel="stylesheet">
<style>
  :root {
    --page-bg: #c4c4c4;
    --card-white: #ffffff;
    --card-black: #0d0d0d;
    --ink: #1a1a1a;
    --ink-soft: #3a3a3a;
    --paper-text: #f4f4f4;
  }
  * { box-sizing: border-box; margin: 0; padding: 0; }
  html, body {
    width: 1200px; height: 1000px; overflow: hidden;
    background: var(--page-bg);
    font-family: "Poppins", sans-serif;
  }
  .canvas {
    position: relative; width: 1200px; height: 1000px;
    display: flex; align-items: center; justify-content: center; gap: 80px;
  }
  .card {
    position: relative; width: 500px; height: 280px;
    box-shadow: 0 6px 18px rgba(0,0,0,0.18);
    overflow: hidden;
  }
  /* Front */
  .card-front { background: var(--card-white); color: var(--ink); }
  .identity { position: absolute; left: 36px; top: 36px; display: flex; gap: 12px; }
  .identity-bar { width: 8px; height: 36px; background: var(--ink); }
  .person-name { font-size: 18px; font-weight: 600; letter-spacing: 0.5px; line-height: 1.1; text-transform: uppercase; }
  .person-title { font-size: 9px; font-weight: 500; letter-spacing: 0.6px; text-transform: uppercase; margin-top: 3px; }
  .address { position: absolute; left: 36px; top: 94px; font-size: 11px; line-height: 1.55; color: var(--ink-soft); }
  .contact-list { position: absolute; left: 36px; bottom: 46px; list-style: none; font-size: 11px; color: var(--ink-soft); }
  .contact-list li { display: flex; align-items: center; gap: 8px; line-height: 1.8; }
  .contact-list svg { width: 10px; height: 10px; fill: var(--ink); }
  .front-brand {
    position: absolute; right: 34px; bottom: 52px;
    font-size: 16px; font-weight: 600; letter-spacing: 1.5px;
    text-transform: uppercase; color: var(--ink);
  }
  .footer-band { position: absolute; left: 0; right: 0; bottom: 0; height: 22px; background: var(--card-black); }
  .footer-mark { position: absolute; left: 36px; top: 7px; width: 8px; height: 8px; background: var(--paper-text); }
  /* Back */
  .card-back { background: var(--card-black); display: flex; align-items: center; justify-content: center; }
  .back-brand {
    font-size: 24px; font-weight: 500; letter-spacing: 3px;
    text-transform: uppercase; color: var(--paper-text);
  }
</style>
</head>
<body>
<main class="canvas">
  <section class="card card-front" aria-label="Business card front">
    <div class="identity">
      <span class="identity-bar"></span>
      <div>
        <h1 class="person-name">Travis Whitlow</h1>
        <p class="person-title">Managing Partner</p>
      </div>
    </div>
    <p class="address">4136 NE 19th Ter.<br>Ocala, FL 34470</p>
    <ul class="contact-list">
      <li>
        <svg viewBox="0 0 10 10" aria-hidden="true"><rect x="2.5" y="0" width="5" height="10" rx="1"/><rect x="3.5" y="1.2" width="3" height="6.5" fill="#fff"/></svg>
        561-374-9186
      </li>
      <li>
        <svg viewBox="0 0 10 10" aria-hidden="true"><rect x="0" y="1.5" width="10" height="7" rx="1"/><path d="M0.6 2.2 L5 5.6 L9.4 2.2" stroke="#fff" stroke-width="0.9" fill="none"/></svg>
        travis48@quillnet-mail.com
      </li>
    </ul>
    <p class="front-brand">Emberfall Capital</p>
    <div class="footer-band"><span class="footer-mark"></span></div>
  </section>

  <section class="card card-back" aria-label="Business card back">
    <p class="back-brand">Emberfall Capital</p>
  </section>
</main>
</body>
</html>
```